Cause bitches need love too!

I am creating an ad campaign. It will be a series of featured dogs in our shelter and they will contain a picture of the dog wich should be big enough to see on a yard sign and will change every week. I am placing the signs so that they lead you to the shelter. This is why I am also including the copy that says "you're almost there".

I have 4 tag lines:

1. Find unconditional Love.
2. She'll Love you furever!
3. He'll always listen.
4. Meet your new BFF

You're almost there 217 W Marlowe Ave
Open 10 - 7/Tues-Sat

The dimensions for the sign are 24" wide and 18" high

Every week we will have a different picture of a different dog (hopefully last week's dog gets adopted). Anyhow, I am printing out yard signs, meaning that instead of printing 160 different signs it would be ideal just to replace the photo. So far the copy that is permanent is: "You're almost there. 217 W. Marlowe Ave."

I could silhouette the image of the dog as well and super impose it on the sign, that's also a consideration, but ideally if I could have 4 tag lines I could print 40 signs of each and just replace the photo manually each week from my printer that would save costs.
Updates

Not enough designs to chose from and I edited the brief and committed to pay no matter what to increase the amount of designs as per your suggestions.

Target Market(s)

Animal lovers

Industry/Entity Type

Campaign

Font styles to use
Sans Serif

Colors

Designer to choose colors to be used in the design.

Requirements
Must have
• The dimensions for the sign are 24" wide and 18" high
Nice to have
• I want the signs to be hip, they should have a positive feel to them. You can alter the photos if you like. I am even open to new copy if you think something else works better.

```html
<!DOCTYPE html>
<html lang="en">
<head>
<meta charset="utf-8">
<title>Find unconditional Love – Shelter Yard Sign</title>
<link rel="stylesheet" href="https://fonts.googleapis.com/css2?family=Itim&display=swap">
<style>
  :root {
    --page: #e8e8e4;
    --paper: #ffffff;
    --forest-deep: #050b08;
    --forest: #1c3d2b;
    --headline: #e8a040;
    --accent: #d4861c;
    --address: #7a3a12;
    --wood-dark: #7a4418;
    --wood: #a5642a;
    --wood-light: #c07a3a;
  }
  * { margin: 0; padding: 0; box-sizing: border-box; }
  html, body { width: 900px; height: 1200px; overflow: hidden; background: var(--page); }
  /* 24in x 18in yard sign, 4:3 landscape */
  .sign {
    position: absolute;
    left: 0; top: 262px;
    width: 900px; height: 675px;
    background: var(--paper);
    overflow: hidden;
    font-family: "Itim", "Trebuchet MS", sans-serif;
  }
  .backdrop {
    position: absolute;
    left: 16px; top: 16px;
    width: 868px; height: 480px;
    background: linear-gradient(120deg, var(--forest-deep) 0%, #0c1f15 40%, var(--forest) 100%);
  }
  .frame {
    position: absolute;
    left: 70px; top: 36px;
    width: 380px; height: 474px;
    background: linear-gradient(135deg, var(--wood-light) 0%, var(--wood) 45%, var(--wood-dark) 100%);
    box-shadow: 0 12px 18px rgba(0,0,0,0.45), inset 0 0 0 2px rgba(60,30,10,0.5);
  }
  .frame svg { position: absolute; inset: 0; }
  .dog-photo {
    position: absolute;
    left: 54px; top: 54px;
    width: 272px; height: 366px;
    background: radial-gradient(ellipse at 55% 45%, #c08a4a 0%, #8a6030 35%, #9c9a9a 70%, #b8b6b8 100%);
    box-shadow: inset 0 0 0 2px rgba(200,150,80,0.6);
  }
  .headline {
    position: absolute;
    left: 470px; top: 130px; width: 414px;
    text-align: center;
    color: var(--headline);
    font-size: 58px;
    line-height: 58px;
    font-weight: 400;
  }
  .directions {
    position: absolute;
    left: 470px; top: 522px; width: 414px;
    text-align: center;
  }
  .directions .lead { color: var(--accent); font-size: 24px; line-height: 32px; }
  .directions .details { color: var(--address); font-size: 25px; line-height: 33px; margin-top: 6px; }
  .rule {
    position: absolute;
    left: 613px; top: 650px;
    width: 128px; height: 4px;
    background: var(--accent);
  }
</style>
</head>
<body>
<main class="sign">
  <div class="backdrop"></div>
  <div class="frame">
    <svg width="380" height="474" viewBox="0 0 380 474" aria-hidden="true">
      <g stroke="rgba(70,35,10,0.55)" stroke-width="1.5">
        <line x1="0" y1="0" x2="54" y2="54"/>
        <line x1="380" y1="0" x2="326" y2="54"/>
        <line x1="0" y1="474" x2="54" y2="420"/>
        <line x1="380" y1="474" x2="326" y2="420"/>
      </g>
    </svg>
    <div class="dog-photo" role="img" aria-label="Studio portrait of the featured shelter dog, a tan and black mixed breed tilting its head"></div>
  </div>
  <h1 class="headline">Find<br>unconditional<br>Love.</h1>
  <section class="directions">
    <p class="lead">You’re almost there:</p>
    <p class="details">217 W Marlowe Ave<br>Open Tues - Sat 10am - 7pm</p>
  </section>
  <div class="rule"></div>
</main>
</body>
</html>
```